Social Business Consultancy

Makoro Ventures is a start up consultancy but with a difference: were non-corporate. We work in the field of economic development in low income countries and we focus on entrepreneurship but with a social and or environmental mission.

The type of projects we work on are innovative, ground breaking, different, edgy and bold. We are young, determined, , unreasonnable and undeterred by challenges.
We want our website to convey these ideas.
Updates

Hello,

Could you please include the option of having the website in two languages. Thank you.

Please note that new files have been added to the project brief.

- FrontPage  Main Photo (Grey dirt Road)
- WordCloud Photo to be used on the home page (as a small image )

The website should keep these colour tones.

Thank you !

Hello,

Wireframes have been uploaded. Please use as an indication.

Thanks,
n.

Target Market(s)

Governments, development agencies, social investors, NGOs, banks and social entrepreneurs.

Industry/Entity Type

Consulting

Requirements
Must have
• We already have a logo and business cards (provided). We want the website to look professional, yet simple with a maximum of two or three colours. We want the look to be seamless. There is no need for too many boxes or categories.
Nice to have
• We want bold, edgy, modern  and professional look .
• Examples:
• http://www.brightlanecollective.org/
• http://www.pagemorph.com/
• http://www.tallyhiring.co.nz/
Should not have
• The design should not use old style fonts.

```html
<!DOCTYPE html>
<html lang="en">
<head>
<meta charset="utf-8">
<title>Makoro Ventures</title>
<link rel="stylesheet" href="https://fonts.googleapis.com/css2?family=Arimo:wght@400;700&family=Didact+Gothic&display=swap">
<style>
  :root {
    --lime: #c9dc2b;
    --lime-light: #dde97a;
    --panel: #ececec;
    --page: #ffffff;
    --ink: #4b4b4b;
    --nav-ink: #575757;
    --bullet: #777777;
  }
  * { box-sizing: border-box; margin: 0; padding: 0; }
  html, body { width: 999px; height: 1200px; overflow: hidden; background: var(--page); }
  body { font-family: "Arimo", Arial, sans-serif; color: var(--ink); position: relative; }

  .site {
    position: absolute; left: 22px; top: 0; width: 953px; height: 1200px;
    background: var(--page);
    box-shadow: 0 0 18px rgba(0,0,0,0.18);
  }
  .masthead {
    position: absolute; left: 13px; top: 12px; width: 927px; height: 90px;
    background: var(--panel);
  }
  .brand {
    position: absolute; left: 22px; top: 22px;
    display: flex; align-items: center; gap: 12px;
    font-family: "Didact Gothic", sans-serif; font-size: 42px; color: var(--nav-ink);
  }
  .brand-mark { width: 32px; height: 32px; background: var(--lime); }

  .main-nav {
    position: absolute; left: 0; top: 114px; width: 953px; height: 36px;
    background: var(--lime);
    display: flex; justify-content: center; align-items: center;
  }
  .main-nav a {
    font-weight: 700; font-size: 15px; color: var(--nav-ink); text-decoration: none;
    padding: 0 26px;
  }
  .main-nav .divider { width: 2px; height: 22px; background: var(--nav-ink); }

  .content {
    position: absolute; left: 13px; top: 164px; width: 927px; height: 1026px;
    background: var(--panel);
  }
  .section-title {
    position: absolute; left: 80px;
    font-weight: 700; font-size: 17px; color: var(--lime);
  }
  .section-title.small { font-size: 15px; }
  .point {
    position: absolute; left: 80px; width: 817px;
    font-size: 15px; line-height: 19px; text-align: justify;
  }
  .point.marked::before {
    content: ""; position: absolute; left: -50px; top: 0;
    width: 17px; height: 17px; border-radius: 50%;
    border: 2px solid var(--bullet); background: #f4f4f4;
  }
  .statement {
    position: absolute; left: 29px; top: 266px; width: 868px;
    font-size: 15px; line-height: 19px; color: var(--lime); text-align: justify;
  }

  .banner {
    position: absolute; left: 0; top: 348px; width: 927px; height: 298px;
    background: radial-gradient(ellipse 30% 45% at 50% 52%, var(--lime-light) 0%, var(--lime) 100%);
  }
</style>
</head>
<body>
<div class="site">
  <header class="masthead">
    <div class="brand"><span>Makoro</span><span class="brand-mark"></span></div>
  </header>

  <nav class="main-nav">
    <a href="#">Home</a>
    <span class="divider"></span>
    <a href="#">Contact Us</a>
  </nav>

  <main class="content">
    <h2 class="section-title" style="top:32px">Welcome</h2>
    <p class="point marked" style="top:71px">Do you believe that you have the power to be the vehicle of change?</p>
    <p class="point marked" style="top:126px">Do you want to be part of the process that will help increase the quality of the lives of millions of people living under the poverty line?</p>
    <p class="point marked" style="top:198px">Do you want to invest in projects that aim to achieve profitability, social empowerment and environmental sustainability?</p>

    <p class="statement">We are passionate about change. We believe that energy is at the center of the development solution. We work so that even the poorest family in rural Africa is able to get affordable clean energy. We believe that we can make a difference. Can you ?</p>

    <div class="banner" role="img" aria-label="Word cloud banner of development themes around a fingerprint illustration"></div>

    <h2 class="section-title" style="top:677px">About</h2>
    <p class="point marked" style="top:717px">Makoro is a start-up social enterprise that contributes to poverty reduction by channeling human and investment capital in projects that offer increased access to clean energy products for the Bottom of the Pyramid.</p>

    <h2 class="section-title" style="top:773px">Mission Statement</h2>
    <p class="point marked" style="top:813px">To contribute to poverty reduction by channeling human and investment capital in projects that offer increased access to clean energy products for the Bottom of the Pyramid (“BOP”).</p>

    <h2 class="section-title small" style="top:868px">Objectives</h2>
    <p class="point marked" style="top:901px">We thrive for a triple bottom line approach of balancing commercial, social and environmental objectives.</p>
    <p class="point" style="top:937px">We aim to promote and expand the access to clean energy products to the Bottom of the Pyramid.</p>
    <p class="point" style="top:974px">We connect investors, microfinance institutions and clean energy providers.</p>
  </main>
</div>
</body>
</html>
```